Website for new child psychology practice

New clinical psychology practice in NSW Australia, specialising in work with children, adolescents and families. I would like to feature the colours in the logo, which was recently designed by pixelmesa designer Odette.
I am seeking a professional looking page, which is easy to navigate and is colourful and playful but not childish.
Target Market(s)
Parents and professionals
Industry/Entity Type
Health
Coding
Coded - Design and coding required
Number of Pages Required
1 page
Font styles to use
Serif
Requirements
Must have
- Pages for 'About us' 'Services' 'Fees and information' 'Contact us'
Should not have
- Childish stock photos

```html
<!DOCTYPE html>
<html lang="en">
<head>
<meta charset="utf-8">
<title>Dr Helen Marsh – Clinical Psychologist</title>
<link href="https://fonts.googleapis.com/css2?family=Lato:wght@400;700&family=Roboto:wght@300;400;500;700;900&display=swap" rel="stylesheet">
<style>
:root{
  --purple:#a3327f;
  --purple-dark:#8c2a6e;
  --orange:#ee8440;
  --sand:#f4c67e;
  --cream:#fcf1e3;
  --grey:#efefef;
  --ink:#222;
  --text:#333;
  --black:#0a0a0a;
}
*{box-sizing:border-box;margin:0;padding:0}
html,body{width:1200px;height:4170px;overflow:hidden}
body{font-family:"Lato",sans-serif;color:var(--text);background:#fff;position:relative}
.abs{position:absolute}
.btn{position:absolute;display:flex;align-items:center;justify-content:center;background:var(--orange);color:#fff;border-radius:30px;font-family:"Roboto",sans-serif;font-weight:700;font-size:13px;text-transform:uppercase;letter-spacing:.2px}
.topline{top:0;left:0;width:1200px;height:6px;background:var(--purple)}
.brand{display:flex;align-items:center;gap:8px}
.brand-dot{width:40px;height:40px;border-radius:50%;background:var(--purple)}
.brand-name{font-family:"Lato",sans-serif;font-weight:400;color:#555;font-size:27px;letter-spacing:.5px;line-height:1}
.brand-sub{font-family:"Lato",sans-serif;font-weight:400;color:#555;font-size:10px;letter-spacing:3px;display:block;margin-top:2px}
.contact-item{display:flex;align-items:center;gap:14px;font-size:14px;color:#333}
.ring{width:42px;height:42px;border:1.5px solid var(--purple);border-radius:50%;display:flex;align-items:center;justify-content:center}
.nav{top:107px;left:0;width:1200px;height:68px;background:var(--sand);display:flex;align-items:center;font-size:15px;color:#333}
.nav a{text-decoration:none;color:#333;position:absolute;top:0;height:68px;display:flex;align-items:center}
.nav .active{background:var(--purple);color:#fff;left:0;width:184px;justify-content:center}
.search{position:absolute;left:895px;top:18px;width:190px;border-bottom:1px solid #c9a56a;font-size:14px;padding-bottom:6px;color:#444}
.hero{top:175px;left:0;width:1200px;height:740px;background:linear-gradient(100deg,#7a7a7a 0%,#6d6d6d 40%,#808080 70%,#9a9a9a 100%)}
.hero h1{position:absolute;left:110px;top:132px;color:#fff;font-family:"Roboto",sans-serif;line-height:1.18}
.hero h1 b{font-weight:900;font-size:60px;display:block}
.hero h1 span{font-weight:400;font-size:60px;display:block}
.hero p{position:absolute;left:110px;top:298px;color:#fff;font-size:21px}
.heading{font-family:"Roboto",sans-serif;font-weight:500;font-size:34px;color:var(--ink);display:flex;align-items:center;gap:10px}
.mark{width:34px;height:34px;border-radius:50%;background:var(--purple)}
.body-text{font-size:13.6px;line-height:25.8px;text-align:justify;color:#333}
.services{top:1475px;left:0;width:1200px;height:515px;background:var(--grey)}
.card{position:absolute;top:182px;width:262px;height:208px;background:#fff;border:1px solid #c58ab0;border-radius:28px 4px 28px 4px;display:flex;flex-direction:column;align-items:center;justify-content:flex-end;padding-bottom:24px;font-family:"Roboto",sans-serif;font-size:18px;text-align:center;line-height:28px;color:#222}
.card svg{margin-bottom:18px}
.card.featured{background:var(--purple);color:#fff;border-color:var(--purple)}
.contact{top:2572px;left:0;width:1200px;height:532px;background:var(--cream)}
.field{position:absolute;height:56px;border:1px solid #bbb;border-radius:28px;background:#fff;font-family:Arial,sans-serif;font-size:13px;color:#444;display:flex;align-items:center;padding-left:26px;box-shadow:0 2px 4px rgba(0,0,0,.08)}
.footer{top:3780px;left:0;width:1200px;height:390px;background:var(--black);color:#fff}
.footer h4{font-family:"Roboto",sans-serif;font-weight:700;font-size:19px;margin-bottom:12px}
.footer ul{list-style:none;font-size:14.5px;line-height:26px}
.footer li::before{content:"»";margin-right:12px}
.social{display:flex;gap:8px}
.social span{width:35px;height:35px;border:1.5px solid #fff;border-radius:50%}
.copy{position:absolute;left:113px;top:330px;width:974px;border-top:1px solid #333;padding-top:14px;text-align:center;font-size:14px}
</style>
</head>
<body>
<div class="abs topline"></div>

<header>
  <div class="abs brand" style="left:113px;top:32px">
    <div class="brand-dot"></div>
    <div><span class="brand-name">DR HELEN MARSH</span><span class="brand-sub">CLINICAL PSYCHOLOGIST</span></div>
  </div>
  <div class="abs contact-item" style="left:480px;top:38px">
    <div class="ring"><svg width="16" height="20" viewBox="0 0 16 20"><path d="M8 1a6 6 0 0 0-6 6c0 5 6 12 6 12s6-7 6-12a6 6 0 0 0-6-6z" fill="none" stroke="#ee8440" stroke-width="1.4"/><circle cx="8" cy="7" r="2" fill="none" stroke="#ee8440" stroke-width="1.4"/></svg></div>NSW Australia
  </div>
  <div class="abs contact-item" style="left:697px;top:38px">
    <div class="ring"><svg width="20" height="20" viewBox="0 0 20 20"><path d="M4 2l3 0 2 4-2 2c1 2 3 4 5 5l2-2 4 2v3c0 1-1 2-2 2C9 18 2 11 2 4c0-1 1-2 2-2z" fill="none" stroke="#ee8440" stroke-width="1.3"/></svg></div>+61 (02) 5550 1234
  </div>
  <div class="btn" style="left:930px;top:36px;width:158px;height:44px">Free Consultation</div>
</header>

<nav class="abs nav">
  <a class="active" href="#">HOME</a>
  <a style="left:223px" href="#">ABOUT US</a>
  <a style="left:352px" href="#">SERVICES</a>
  <a style="left:476px" href="#">FEES AND INFORMATION</a>
  <a style="left:713px" href="#">CONTACT US</a>
  <div class="search">Search<svg style="position:absolute;right:4px;top:2px" width="14" height="14" viewBox="0 0 14 14"><circle cx="6" cy="6" r="4.5" fill="none" stroke="#333" stroke-width="2"/><path d="M9.5 9.5l3.5 3.5" stroke="#333" stroke-width="2"/></svg></div>
</nav>

<section class="abs hero" role="img" aria-label="Photo of a psychologist taking notes during a session with a teenage girl on a sofa">
  <h1><b>CHILD, ADOLESCENT</b><span>FAMILY PSYCHOLOGY</span></h1>
  <p>Our service is located at NSW Australia</p>
  <div class="btn" style="left:113px;top:355px;width:159px;height:45px">Free Consultation</div>
</section>
<svg class="abs" style="left:0;top:690px" width="1200" height="260" viewBox="0 0 1200 260">
  <path d="M0 130 C150 30 400 60 630 95 C420 110 200 150 0 215 Z" fill="var(--purple)"/>
  <path d="M0 215 C200 150 420 110 630 95 C800 80 1000 160 1200 80 L1200 260 L0 260 Z" fill="#fff"/>
  <path d="M570 25 C760 110 1000 150 1200 40 L1200 150 C1050 210 900 190 800 150 C720 110 640 70 570 25 Z" fill="var(--sand)"/>
  <path d="M800 150 C900 190 1050 210 1200 150 L1200 160 C1060 230 900 220 800 150 Z" fill="var(--black)"/>
</svg>

<section id="about">
  <svg class="abs" style="left:100px;top:888px" width="500" height="500" viewBox="0 0 500 500"><path d="M250 5 A245 245 0 0 1 250 495" fill="none" stroke="var(--orange)" stroke-width="4"/></svg>
  <div class="abs" role="img" aria-label="Photo of a psychologist talking with a young girl at a table" style="left:108px;top:905px;width:485px;height:470px;border-radius:50%;background:linear-gradient(135deg,#e9e3dc,#c9c0b6)"></div>
  <h2 class="abs heading" style="left:630px;top:945px"><span class="mark"></span>ABOUT US</h2>
  <p class="abs body-text" style="left:630px;top:1018px;width:455px">Lorem ipsum dolor sit amet, consectetur adipiscing elit, sed do eiusmod tempor incididunt ut labore et dolore magna aliqua. Ut enim ad minim veniam, quis nostrud exercitation ullamco laboris nisi ut aliquip ex ea commodo consequat. Duis aute irure dolor in reprehenderit in voluptate velit esse cillum dolore eu fugiat nulla pariatur. Excepteur sint occaecat cupidatat non proident, sunt in culpa qui officia deserunt mollit anim id est laborum. Sed ut perspiciatis unde omnis iste natus error sit voluptatem accusantium doloremque laudantium, totam rem.</p>
  <div class="btn" style="left:630px;top:1285px;width:126px;height:45px">Learn More</div>
</section>

<section class="abs services" id="services">
  <h2 class="heading" style="position:absolute;left:0;width:1200px;top:90px;justify-content:center"><span class="mark"></span>OUR SERVICES</h2>
  <div class="card" style="left:178px">
    <svg width="80" height="80" viewBox="0 0 80 80" fill="none" stroke="var(--purple)" stroke-width="2"><path d="M22 70V56c-8-6-10-14-8-24 4-16 26-22 38-10 6 6 7 13 6 18l6 10-6 2v8c0 4-4 6-8 5l-6-1v6"/><circle cx="38" cy="34" r="8"/><circle cx="38" cy="34" r="2"/></svg>
    Psychological assessment<br>and intervention</div>
  <div class="card featured" style="left:469px">
    <svg width="96" height="70" viewBox="0 0 96 70" fill="none" stroke="#fff" stroke-width="2.5"><path d="M4 44c24-28 64-28 88 0-24 28-64 28-88 0z"/><circle cx="48" cy="44" r="14"/><path d="M42 44l4 4 8-8"/><path d="M36 6v8M48 4v8M60 6v8"/></svg>
    Clinical Supervision</div>
  <div class="card" style="left:759px">
    <svg width="80" height="80" viewBox="0 0 80 80" fill="none" stroke="var(--purple)" stroke-width="2"><path d="M16 6h30l12 12v56H16z"/><path d="M46 6v12h12"/><path d="M24 40h24M24 48h20M24 56h14M24 64h10"/><path d="M50 62l18-24 5 4-18 24-7 2z"/></svg>
    Forensic Reports</div>
</section>

<section id="about-helen">
  <h2 class="abs heading" style="left:113px;top:2092px"><span class="mark"></span>ABOUT HELEN</h2>
  <p class="abs body-text" style="left:113px;top:2163px;width:455px">Lorem ipsum dolor sit amet, consectetur adipiscing elit, sed do eiusmod tempor incididunt ut labore et dolore magna aliqua. Ut enim ad minim veniam, quis nostrud exercitation ullamco laboris nisi ut aliquip ex ea commodo consequat. Duis aute irure dolor in reprehenderit in voluptate velit esse cillum dolore eu fugiat nulla pariatur. Excepteur sint occaecat cupidatat non proident, sunt in culpa qui officia deserunt mollit anim id est laborum. Sed ut perspiciatis unde omnis iste natus error sit voluptatem accusantium doloremque laudantium, totam rem.</p>
  <div class="btn" style="left:113px;top:2430px;width:126px;height:46px">Learn More</div>
  <svg class="abs" style="left:690px;top:2072px" width="360" height="425" viewBox="0 0 360 425" role="img" aria-label="Portrait photo of the psychologist smiling at her desk">
    <defs><linearGradient id="pg" x1="0" y1="0" x2="1" y2="1"><stop offset="0" stop-color="#e7e4e0"/><stop offset="1" stop-color="#b8bcc2"/></linearGradient></defs>
    <path d="M180 5a175 175 0 1 1-75 333L20 420l40-110A175 175 0 0 1 180 5z" fill="url(#pg)"/>
  </svg>
</section>

<section class="abs contact" id="contact">
  <h2 class="heading" style="position:absolute;left:0;width:1200px;top:63px;justify-content:center"><span class="mark"></span>CONTACT US</h2>
  <div class="field" style="left:170px;top:150px;width:420px">First Name :</div>
  <div class="field" style="left:608px;top:150px;width:422px">Last Name :</div>
  <div class="field" style="left:170px;top:230px;width:420px">Email :</div>
  <div class="field" style="left:608px;top:230px;width:422px">Phone :</div>
  <div class="field" style="left:170px;top:313px;width:860px">Message :</div>
  <div class="btn" style="left:517px;top:408px;width:168px;height:54px;font-size:16px;font-weight:500">Submit</div>
</section>

<section id="fees">
  <h2 class="abs heading" style="left:113px;top:3200px"><span class="mark"></span>FEES AND INFORMATION</h2>
  <p class="abs body-text" style="left:113px;top:3270px;width:455px">Lorem ipsum dolor sit amet, consectetur adipiscing elit, sed do eiusmod tempor incididunt ut labore et dolore magna aliqua. Ut enim ad minim veniam, quis nostrud exercitation ullamco laboris nisi ut aliquip ex ea commodo consequat. Duis aute irure dolor in reprehenderit in voluptate velit esse cillum dolore eu fugiat nulla pariatur. Excepteur sint occaecat cupidatat non proident, sunt in culpa qui officia deserunt mollit anim id est laborum. Sed ut perspiciatis unde omnis iste natus error sit voluptatem accusantium doloremque laudantium, totam rem.</p>
  <div class="btn" style="left:113px;top:3537px;width:126px;height:46px">Learn More</div>
  <div class="abs" role="img" aria-label="Decorative cluster of droplet shapes filled with sunset landscape imagery" style="left:605px;top:3190px;width:485px;height:400px;border-radius:50%;background:radial-gradient(circle,#7a3a5c 0%,#a3327f 45%,rgba(163,50,127,0) 72%)"></div>
</section>

<svg class="abs" style="left:0;top:3600px" width="1200" height="190" viewBox="0 0 1200 190">
  <path d="M0 0 C120 110 380 120 560 80 C400 130 160 130 0 85 Z" fill="var(--purple)"/>
  <path d="M0 85 C160 130 400 130 560 80 C760 40 1000 50 1200 10 L1200 190 L0 190 Z" fill="var(--black)"/>
  <path d="M570 180 C800 150 1000 120 1200 20 L1200 80 C1060 150 860 185 570 180 Z" fill="var(--sand)"/>
</svg>

<footer class="abs footer">
  <div class="abs brand" style="left:113px;top:120px">
    <div class="brand-dot" style="width:36px;height:36px"></div>
    <div><span class="brand-name" style="color:#fff;font-size:25px">DR HELEN MARSH</span><span class="brand-sub" style="color:#fff;font-size:9px">CLINICAL PSYCHOLOGIST</span></div>
  </div>
  <div class="abs social" style="left:113px;top:180px"><span></span><span></span><span></span><span></span><span></span></div>
  <div class="abs" style="left:450px;top:92px"><h4>Quick Links</h4><ul><li>Home</li><li>About Us</li><li>Services</li><li>Fees and Information</li><li>Contact Us</li></ul></div>
  <div class="abs" style="left:680px;top:92px"><h4>Other Links</h4><ul><li>Terms &amp; Conditions</li><li>Privacy Policy</li><li>About Us</li><li>Support</li></ul></div>
  <div class="abs" style="left:899px;top:92px;font-size:14.5px;line-height:26px">
    <h4>Contact us</h4>
    <div style="display:flex;gap:8px"><svg width="14" height="18" viewBox="0 0 14 18" style="margin-top:4px"><path d="M7 0a6 6 0 0 0-6 6c0 5 6 12 6 12s6-7 6-12a6 6 0 0 0-6-6z" fill="#fff"/><circle cx="7" cy="6" r="2" fill="#000"/></svg><div>Dr.Helen Marsh<br>NSW Australia</div></div>
    <div style="display:flex;gap:8px;margin-top:16px;align-items:center"><svg width="15" height="15" viewBox="0 0 20 20"><path d="M4 1h4l2 5-3 2c1 2 3 4 5 5l2-3 5 2v4c0 2-1 3-3 3C8 19 1 12 1 4c0-2 1-3 3-3z" fill="#fff"/></svg>+61 (02) 5550 1234</div>
    <div style="display:flex;gap:8px;margin-top:16px;align-items:center"><svg width="16" height="12" viewBox="0 0 16 12"><rect width="16" height="12" rx="1" fill="#fff"/><path d="M0 1l8 6 8-6" fill="none" stroke="#000" stroke-width="1.3"/></svg>info@drhelenmarsh.com</div>
  </div>
  <div class="copy">©Copyrights 2024 Dr.Helen Marsh &nbsp; | &nbsp; All Rights Reserved</div>
</footer>
</body>
</html>
```